Tillard Environmental Projects New Website Design

I need a new website for a Environmental Project Company based in Sydney Australia, working throughout South East Asia.I've attached the company logo, please try & incorporate these colours or use complimentary colours. I've attached a word doc with design brief.I'm going to use Wix, so please ensure files are suitable.Thankyou.

Number of Pages Required

5+ page

Colors

Designer to choose colors to be used in the design.

Requirements
Must have
• Refer to Word Document
Nice to have
• Refer to Word Document
Should not have
• Not to be dark

```html
<!DOCTYPE html>
<html lang="en">
<head>
<meta charset="utf-8">
<title>Tillard Environmental Projects</title>
<link href="https://fonts.googleapis.com/css2?family=Montserrat:wght@400;500;600;700;800&display=swap" rel="stylesheet">
<style>
:root{
  --green:#4f7d1f;
  --green-dark:#3f611a;
  --footer:#46631f;
  --ink:#2d2d2d;
  --muted:#8a8a8a;
  --light:#f4f4f4;
  --grey:#ebebeb;
  --white:#ffffff;
  --card-line:#dcdcdc;
}
*{box-sizing:border-box;margin:0;padding:0}
html,body{width:1200px;height:4358px;overflow:hidden}
body{font-family:"Montserrat",sans-serif;color:var(--ink);background:var(--white);position:relative}
section,header,footer{position:absolute;left:0;width:1200px;overflow:hidden}
.abs{position:absolute}
.photo{position:absolute;display:block}
.heading{position:absolute;left:0;width:100%;text-align:center;text-transform:uppercase}
.heading .big{display:block;font-size:36px;font-weight:800;color:var(--green);letter-spacing:2px}
.heading .small{display:block;font-size:22px;font-weight:700;color:var(--ink);letter-spacing:1.5px;margin-top:12px}
.body-text{font-size:14px;line-height:23px;color:var(--muted)}
.circle-btn{width:32px;height:32px;border-radius:50%;border:2px solid #9a9a9a;display:flex;align-items:center;justify-content:center}
.circle-btn.filled{background:var(--green-dark);border-color:var(--green-dark)}

/* header */
.site-header{top:0;height:160px;background:var(--white);border-top:7px solid var(--green)}
.brand{position:absolute;left:64px;top:36px;display:flex;align-items:center;gap:14px}
.brand-dot{width:74px;height:74px;border-radius:50%;background:var(--green)}
.brand-name{font-size:19px;font-weight:700;color:var(--green);line-height:22px;letter-spacing:1.5px;text-transform:uppercase}
.brand-name small{display:block;font-size:12px;letter-spacing:1px;line-height:16px}
.nav{position:absolute;right:66px;top:72px;display:flex;gap:30px;font-size:16px;font-weight:500;color:var(--green);text-transform:uppercase;letter-spacing:.5px}

/* hero */
.hero{top:160px;height:436px}
.hero-title{position:absolute;left:560px;width:570px;top:150px;text-align:center;color:var(--white);font-size:37px;font-weight:700;letter-spacing:3px;line-height:44px;text-transform:uppercase;text-shadow:0 2px 6px rgba(0,0,0,.35)}

/* about */
.about{top:596px;height:755px;background:var(--grey)}
.about .intro{position:absolute;left:300px;width:600px;top:150px;text-align:center}
.feature-card{position:absolute;top:264px;width:407px;height:462px;background:var(--white);border:1px solid var(--card-line);box-shadow:0 2px 6px rgba(0,0,0,.08)}
.feature-card .photo{left:0;top:0;width:100%;height:250px}
.feature-card h3{position:absolute;left:26px;top:272px;font-size:15px;font-weight:700}
.feature-card p{position:absolute;left:26px;right:26px;top:300px;font-size:13px;line-height:19px;color:var(--muted);text-align:justify}
.feature-card .circle-btn{position:absolute;left:26px;top:398px}

/* years */
.years{top:1351px;height:465px;background:var(--white)}
.years .count{position:absolute;left:64px;top:82px;font-size:54px;font-weight:800;color:var(--green-dark);letter-spacing:2px}
.years .tagline{position:absolute;left:64px;top:166px;font-size:25px;font-weight:700;line-height:32px;text-transform:uppercase;letter-spacing:1px}
.years .body-text{position:absolute;left:64px;top:246px;width:412px}
.know-more{position:absolute;left:64px;top:354px;display:flex;align-items:center;gap:14px;font-size:13px;font-weight:600}
.service-tile{position:absolute;width:290px;height:156px;display:flex;flex-direction:column;align-items:center;justify-content:center;gap:20px;color:var(--green);font-size:18px;font-weight:500;letter-spacing:1.5px;text-transform:uppercase}
.service-tile.shaded{background:var(--grey)}

/* team */
.team{top:1816px;height:416px;background:var(--grey)}
.lead{position:absolute;left:64px;top:151px;width:238px;height:236px}
.lead-info{position:absolute;left:334px;top:200px;width:320px}
.lead-info h4{font-size:15px;font-weight:700;color:var(--green);letter-spacing:1px}
.lead-info .role{font-size:11px;color:var(--muted);letter-spacing:1px;margin:4px 0 16px}
.member{position:absolute;top:151px;width:204px;height:241px;background:var(--white)}
.member .photo{left:0;top:0;width:100%;height:183px}
.member h4{position:absolute;left:12px;top:194px;font-size:13px;font-weight:700;letter-spacing:.5px}
.member .role{position:absolute;left:12px;top:214px;font-size:10px;color:var(--muted)}

/* testimonials */
.testimonials{top:2232px;height:514px;background:var(--light)}
.quote-card{position:absolute;top:209px;width:511px;height:169px;background:var(--white);border:1px solid var(--card-line)}
.quote-card .qmark{position:absolute;left:22px;top:52px;font-size:60px;line-height:50px;font-weight:800;color:#c9c9c9}
.quote-card p{position:absolute;left:78px;right:40px;top:56px;font-size:14px;line-height:21px;color:var(--muted)}
.quote-card .who{position:absolute;left:78px;top:128px;font-size:12px;font-weight:600}
.avatar{position:absolute;width:80px;height:80px;border-radius:50%;border:4px solid var(--white);box-shadow:0 1px 4px rgba(0,0,0,.2)}
.badge{position:absolute;width:36px;height:36px;border-radius:50%;background:var(--green);display:flex;align-items:center;justify-content:center}
.dots{position:absolute;left:0;width:100%;top:454px;display:flex;justify-content:center;gap:8px}
.dots span{width:11px;height:11px;border-radius:50%;background:var(--ink)}

/* blog */
.blog{top:2746px;height:538px;background:var(--grey)}
.post{position:absolute;top:137px;width:330px;height:366px;background:var(--white);border:1px solid var(--card-line)}
.post .photo{left:0;top:0;width:100%;height:212px}
.post h3{position:absolute;left:18px;top:226px;font-size:13px;font-weight:700}
.post p{position:absolute;left:18px;right:18px;top:246px;font-size:11px;line-height:15px;color:var(--muted)}
.post .circle-btn{position:absolute;left:18px;top:318px;width:28px;height:28px}

/* video + news */
.media{top:3284px;height:372px;background:var(--white)}
.video{left:0;top:0;width:575px;height:372px}
.play{position:absolute;left:222px;top:126px;width:112px;height:112px;border-radius:50%;border:5px solid var(--white);display:flex;align-items:center;justify-content:center}
.news-heading{position:absolute;left:575px;width:625px;top:28px;text-align:center;text-transform:uppercase}
.news-heading .big{display:block;font-size:36px;font-weight:800;color:var(--green);letter-spacing:2px}
.news-heading .small{display:block;font-size:22px;font-weight:700;letter-spacing:1.5px;margin-top:8px}
.news-item{position:absolute;left:619px;width:540px;height:87px}
.news-item .photo{left:0;top:0;width:195px;height:87px}
.news-item h4{position:absolute;left:226px;top:4px;font-size:13px;font-weight:700}
.news-item p{position:absolute;left:226px;top:24px;width:300px;font-size:12px;line-height:17px;color:var(--muted)}
.news-item .date{position:absolute;left:226px;top:66px;font-size:11px;color:var(--muted)}

/* projects */
.projects{top:3656px;height:404px;background:var(--grey)}
.strip{position:absolute;left:0;top:154px;width:1200px;height:229px}
.project-label{position:absolute;left:18px;bottom:18px;color:var(--white)}
.project-label strong{display:block;font-size:14px;font-weight:700;text-transform:uppercase}
.project-label span{font-size:11px}

/* footer */
.site-footer{top:4060px;height:298px;background:var(--footer);color:var(--white)}
.foot-col{position:absolute;top:56px}
.foot-col h5{font-size:14px;font-weight:700;letter-spacing:1px;text-transform:uppercase;margin-bottom:16px}
.foot-col ul{list-style:none;font-size:12px;line-height:22px;opacity:.9}
.foot-brand{position:absolute;left:712px;top:128px;display:flex;align-items:center;gap:10px;opacity:.55}
.foot-brand .dot{width:48px;height:48px;border-radius:50%;background:var(--white)}
.foot-brand span{font-size:14px;font-weight:700;letter-spacing:1px;text-transform:uppercase;line-height:16px}
.contact{position:absolute;left:884px;top:100px;font-size:12px;line-height:20px;opacity:.9}
.contact p{margin-bottom:14px}
</style>
</head>
<body>

<header class="site-header">
  <div class="brand">
    <div class="brand-dot"></div>
    <div class="brand-name">Tillard<small>Environmental</small><small>Projects</small></div>
  </div>
  <nav class="nav"><span>Home</span><span>Who we are</span><span>Services</span><span>Products</span><span>News</span><span>Contact</span></nav>
</header>

<section class="hero">
  <div class="photo" role="img" aria-label="Hands holding a seedling in soil against a soft green background with a butterfly" style="left:0;top:0;width:1200px;height:436px;background:radial-gradient(ellipse at 25% 45%,#b7d98a 0%,#6fae35 35%,#3f8a1f 70%,#2d6a16 100%)"></div>
  <h1 class="hero-title">Save the environment<br>&amp;<br>you will save life &amp; future</h1>
</section>

<section class="about">
  <div class="heading" style="top:43px"><span class="big">Tillard</span><span class="small">Environmental Projects</span></div>
  <p class="intro body-text">Lorem Ipsum is simply dummy text of the printing and typesetting industry. Lorem Ipsum has been the industry's standard dummy text ever since the 1500s, when an unknown printer took a galley book.</p>
  <article class="feature-card" style="left:157px">
    <div class="photo" role="img" aria-label="Hands cupping a glass globe over green grass" style="background:linear-gradient(160deg,#7fbf3f,#3f7f1f 60%,#6a9a3a)"></div>
    <h3>OUR VISION</h3>
    <p>Our Vision is to make it easy for everyone to minimise their environmental impact by providing information, technology, packaged green solutions &amp; helping innovation flourish.</p>
    <div class="circle-btn"><svg width="10" height="12" viewBox="0 0 10 12"><path d="M2 1l6 5-6 5" fill="none" stroke="#555" stroke-width="2"/></svg></div>
  </article>
  <article class="feature-card" style="left:625px">
    <div class="photo" role="img" aria-label="Hand holding a light bulb against warm sunlight" style="background:linear-gradient(135deg,#f5d58a,#c48a2a 45%,#5a4a1a 100%)"></div>
    <h3>OUR MISSION</h3>
    <p>Working with people to minimise the environmental impact of humans on the earth without sacrificing lifestyle and helping innovation flourish.</p>
    <div class="circle-btn filled"><svg width="10" height="12" viewBox="0 0 10 12"><path d="M2 1l6 5-6 5" fill="none" stroke="#fff" stroke-width="2"/></svg></div>
  </article>
</section>

<section class="years">
  <div class="count">10 YEARS</div>
  <div class="tagline">We are helping to<br>save the environment</div>
  <p class="body-text">Lorem Ipsum is simply dummy text of the printing and typesetting industry. Lorem Ipsum has been the industry's standard dummy text ever since the 1500s, when an unknown printer took a galley book.</p>
  <div class="know-more">Know More <span class="circle-btn filled" style="width:26px;height:26px"><svg width="9" height="10" viewBox="0 0 10 12"><path d="M2 1l6 5-6 5" fill="none" stroke="#fff" stroke-width="2"/></svg></span></div>

  <div class="service-tile" style="left:538px;top:53px">
    <svg width="56" height="56" viewBox="0 0 56 56"><path d="M28 50V24M28 34c-10 0-16-8-16-18 10 0 16 6 16 18zM28 30c8 0 14-7 14-16-9 0-14 6-14 16z" fill="none" stroke="#4f7d1f" stroke-width="3"/></svg>
    Sustainable food
  </div>
  <div class="service-tile shaded" style="left:840px;top:53px">
    <svg width="56" height="56" viewBox="0 0 56 56"><path d="M8 28c8-10 22-12 32-4l8-6v20l-8-6c-10 8-24 6-32-4z" fill="none" stroke="#4f7d1f" stroke-width="3"/><circle cx="18" cy="27" r="2" fill="#4f7d1f"/></svg>
    Aquaculture
  </div>
  <div class="service-tile shaded" style="left:538px;top:221px">
    <svg width="56" height="56" viewBox="0 0 56 56"><path d="M8 26L28 10l20 16M14 22v26h28V22" fill="none" stroke="#4f7d1f" stroke-width="3"/><rect x="23" y="32" width="10" height="16" fill="#4f7d1f"/></svg>
    Green walls
  </div>
  <div class="service-tile" style="left:840px;top:221px">
    <svg width="56" height="56" viewBox="0 0 56 56"><path d="M12 46C12 24 26 10 46 8c0 22-14 36-34 38z" fill="#4f7d1f"/><path d="M14 44L38 18" stroke="#fff" stroke-width="2"/></svg>
    Eco gardens
  </div>
</section>

<section class="team">
  <div class="heading" style="top:58px"><span class="big">Tillard's</span><span class="small">Expert Team Mates</span></div>
  <div class="photo lead" role="img" aria-label="Portrait of the founder and CEO" style="background:linear-gradient(180deg,#bdbdbd,#8c8c8c)"></div>
  <div class="lead-info">
    <h4>EVAN KESTREL</h4>
    <div class="role">FOUNDER, CEO</div>
    <p class="body-text">Lorem Ipsum is simply dummy text of the printing and typesetting industry. Lorem Ipsum has been the industry's standard dummy text ever.</p>
  </div>
  <div class="member" style="left:689px">
    <div class="photo" role="img" aria-label="Portrait of a team member wearing sunglasses" style="background:linear-gradient(180deg,#6b5a48,#3a2f26)"></div>
    <h4>MARCUS HALE</h4><div class="role">DESIGNATION</div>
  </div>
  <div class="member" style="left:918px">
    <div class="photo" role="img" aria-label="Portrait of a team member outdoors in greenery" style="background:linear-gradient(180deg,#8aa650,#c9a25a)"></div>
    <h4>NORA WHITFIELD</h4><div class="role">DESIGNATION</div>
  </div>
</section>

<section class="testimonials">
  <div class="heading" style="top:58px"><span class="big">Client's</span><span class="small">Testimonials</span></div>
  <div class="quote-card" style="left:64px">
    <div class="qmark">&ldquo;</div>
    <p>Lorem Ipsum is simply dummy text of the printing and typesetting industry. Lorem Ipsum has...</p>
    <div class="who">Marcus Hale</div>
  </div>
  <div class="quote-card" style="left:622px">
    <div class="qmark">&ldquo;</div>
    <p>Lorem Ipsum is simply dummy text of the printing and typesetting industry. Lorem Ipsum has been the industry's standard dummy text.</p>
    <div class="who">Marcus Hale</div>
  </div>
  <div class="avatar" role="img" aria-label="Client portrait" style="left:280px;top:170px;background:#5a4a3c"></div>
  <div class="badge" style="left:268px;top:160px"><svg width="18" height="18" viewBox="0 0 20 20"><path d="M4 17C4 9 9 4 17 3c0 8-5 13-13 14z" fill="#fff"/></svg></div>
  <div class="avatar" role="img" aria-label="Client portrait" style="left:838px;top:170px;background:#5a4a3c"></div>
  <div class="badge" style="left:826px;top:160px"><svg width="18" height="18" viewBox="0 0 20 20"><path d="M4 17C4 9 9 4 17 3c0 8-5 13-13 14z" fill="#fff"/></svg></div>
  <div class="dots"><span></span><span></span><span></span><span></span></div>
</section>

<section class="blog">
  <div class="heading" style="top:30px"><span class="big">Latest</span><span class="small" style="margin-top:4px">From the blog</span></div>
  <article class="post" style="left:64px">
    <div class="photo" role="img" aria-label="Tall green trees in a forest" style="background:linear-gradient(180deg,#a9d36a,#4f8a24 60%,#2f5e16)"></div>
    <h3>LOREM IPSUM IS SIMPLY</h3>
    <p>Lorem ipsum is simply dummy text of the printing and typesetting industry. Lorem Ipsum has been the industry's standard dummy text ever since the 1500s.</p>
    <div class="circle-btn"><svg width="9" height="10" viewBox="0 0 10 12"><path d="M2 1l6 5-6 5" fill="none" stroke="#555" stroke-width="2"/></svg></div>
  </article>
  <article class="post" style="left:436px">
    <div class="photo" role="img" aria-label="Hands holding a glass globe over grass" style="background:linear-gradient(160deg,#7fbf3f,#3f7f1f 60%,#6a9a3a)"></div>
    <h3>LOREM IPSUM</h3>
    <p>Lorem ipsum is simply dummy text of the printing and typesetting industry. Lorem Ipsum has been the...</p>
    <div class="circle-btn"><svg width="9" height="10" viewBox="0 0 10 12"><path d="M2 1l6 5-6 5" fill="none" stroke="#555" stroke-width="2"/></svg></div>
  </article>
  <article class="post" style="left:805px">
    <div class="photo" role="img" aria-label="Hand holding a light bulb in golden light" style="background:linear-gradient(135deg,#f5d58a,#c48a2a 45%,#5a4a1a 100%)"></div>
    <h3>LOREM IPSUM IS SIMPLY DUMMY...</h3>
    <p>Lorem ipsum is simply dummy text of the printing and typesetting industry. Lorem Ipsum has been the industry's standard dummy text ever since the 1500s.</p>
    <div class="circle-btn filled"><svg width="9" height="10" viewBox="0 0 10 12"><path d="M2 1l6 5-6 5" fill="none" stroke="#fff" stroke-width="2"/></svg></div>
  </article>
</section>

<section class="media">
  <div class="photo video" role="img" aria-label="Video still of an environment project makeover talk with a large sculpture" style="background:linear-gradient(135deg,#6e7a6a,#3c4238 55%,#24261f)">
    <div class="play"><svg width="40" height="46" viewBox="0 0 40 46"><path d="M4 3l33 20L4 43z" fill="#fff"/></svg></div>
  </div>
  <div class="news-heading"><span class="big">Latest</span><span class="small">News by Tillard's</span></div>
  <div class="news-item" style="top:137px">
    <div class="photo" role="img" aria-label="Hands holding a glass globe" style="background:linear-gradient(160deg,#7fbf3f,#3f7f1f)"></div>
    <h4>LOREM IPSUM</h4>
    <p>Lorem ipsum is simply dummy text of the printing and typesetting industry.</p>
    <div class="date">7-Jan-2019</div>
  </div>
  <div class="news-item" style="top:241px">
    <div class="photo" role="img" aria-label="Light bulb in warm sunlight" style="background:linear-gradient(135deg,#f5d58a,#c48a2a 50%,#5a4a1a)"></div>
    <h4>LOREM IPSUM</h4>
    <p>Lorem ipsum is simply dummy text of the printing and typesetting industry.</p>
    <div class="date">7-Jan-2019</div>
  </div>
</section>

<section class="projects">
  <div class="heading" style="top:48px"><span class="big">Recent</span><span class="small" style="margin-top:4px">Projects by us</span></div>
  <div class="strip">
    <div class="photo" role="img" aria-label="Wind turbines in a field under a pale sky" style="left:0;top:0;width:300px;height:229px;background:linear-gradient(180deg,#7d8a80,#3f4a3a)">
      <div class="project-label"><strong>Project title</strong><span>7-Jan-2019</span></div>
    </div>
    <div class="photo" role="img" aria-label="Volunteers planting trees together" style="left:300px;top:0;width:282px;height:229px;background:linear-gradient(180deg,#9cbf7a,#5e7f3e)"></div>
    <div class="photo" role="img" aria-label="Researcher with a tablet among plants" style="left:582px;top:0;width:320px;height:229px;background:linear-gradient(180deg,#c7d9a8,#7f9a5a)"></div>
    <div class="photo" role="img" aria-label="Young tree sapling growing in soil" style="left:902px;top:0;width:298px;height:229px;background:linear-gradient(180deg,#4f6a2a,#2c3a16)"></div>
  </div>
</section>

<footer class="site-footer">
  <div class="foot-col" style="left:64px">
    <h5>Quick Links</h5>
    <ul><li>Home</li><li>Who We Are</li><li>Services</li><li>Products</li><li>News</li><li>Contact</li></ul>
  </div>
  <div class="foot-col" style="left:404px">
    <h5>Products</h5>
    <ul><li>Sustainable Food</li><li>Green Walls</li><li>Eco Gardens</li><li>Living Food Walls</li><li>Aquaculture</li><li>Hydroponic Gardens</li><li>Syndicates Farms</li></ul>
  </div>
  <div class="foot-col" style="left:712px"><h5>Tillard Environmental Projects</h5></div>
  <div class="foot-brand"><div class="dot"></div><span>Tillard<br>Projects</span></div>
  <div class="contact">
    <p>48 Harbour Lane, Suite 12<br>Sydney NSW 2000</p>
    <p>+61 (0)2 5550 0142</p>
    <p>info@tillardenviro.example</p>
  </div>
</footer>

</body>
</html>
```